Architecture office 10 pages brochure for investors

We need a multi-page brochure (10pg) for our small architectural office.
After the long real estate crisis in Greece we're intend to reborn our architectural planning services, to relocate our targets and to communicate the philosophy in the new era of commercial buildings:
Modern architectural language, Highly energy efficient buildings with green and passive oriented design and functional details. Multifamily housing, Office buildings, Hotels, Refurbishment and Interiors from a group of new architects collaborators and an experienced leader.
We need fresh, clever styling with minimal expression and reach meanings. Written in two languages (ENG-GR) the fonts must be compatible. The solution of an digital and non-printed brochure, for on-line sharing, its a possibility and maybe unlock animated and / or AR solutions. The green color -as attached- will be appreciated.

Please provide your professional opinion about the set up of the pages.
An idea given: minimal frontpage, 2-3nd pages "about us" and "contents with photo and some minor text, and every next page refers one selected project with photo and some text for two languages (4-7 pages projects), pages 8-9 listed works-projects, collaborators, clients.
Updates

low design entries -one entry as 4 projects- , low quality, not satisfying the wills

Target Market(s)

investors in commercial buildings, private clients, energy efficiency

Industry/Entity Type

Architecture

Font styles to use
Sans Serif
Other font styles liked:
• greek compatible

Requirements
Must have
• clear - minimal design, photos, illustrations, text, contents.
• some of the projects can find them in attached link,
Nice to have
• dynamic lines, hand drawing sketches
• maybe the building design process: thoughts, sketch, hand design, cad, collaboration with other engineers, 3d renderings, animations ....
Should not have
• art deco, romantic styles, full red or basic contrasting colors (red/green, purple/orange etc)

```html
<!DOCTYPE html>
<html lang="en">
<head>
<meta charset="utf-8">
<title>Lumen Atelier – Brochure Cover Spread</title>
<link rel="stylesheet" href="https://fonts.googleapis.com/css2?family=Montserrat:wght@300;400;500;600;700&display=swap">
<style>
  :root{
    --stage:#3f3f3f;
    --paper:#f4f4f2;
    --lime:#c9d466;
    --lime-block:rgba(204,214,104,.9);
    --olive:#a4b42a;
    --ink:#3a3a3a;
    --muted:#8a8a8a;
    --sky-1:#2f9bd8;
    --sky-2:#7cc6ea;
    --white:#ffffff;
  }
  *{box-sizing:border-box;margin:0;padding:0}
  html,body{width:1200px;height:900px;overflow:hidden}
  body{background:var(--stage);font-family:"Montserrat",sans-serif;position:relative}

  .spread{position:absolute;left:80px;top:82px;width:1040px;height:736px;background:var(--paper);box-shadow:0 20px 50px rgba(0,0,0,.35)}
  .panel{position:absolute;top:0;width:520px;height:736px}
  .panel--back{left:0}
  .panel--front{left:520px;border-left:1px solid rgba(0,0,0,.06)}

  .accent-band{position:absolute;left:22px;top:20px;width:14px;height:696px;background:var(--olive)}

  .hero-photo{position:absolute;left:300px;top:125px;width:480px;height:430px;
    background:linear-gradient(135deg,var(--sky-1) 0%,#4fb0e2 50%,var(--sky-2) 100%)}

  /* contact block */
  .contact{position:absolute;left:70px;top:470px;width:220px;color:var(--ink)}
  .brand{display:flex;align-items:center;gap:7px;color:var(--olive);font-weight:600;font-size:12px;letter-spacing:.02em}
  .brand__dot{width:14px;height:14px;border-radius:50%;border:2px solid var(--olive)}
  .contact__title{margin-top:22px;font-size:15px;font-weight:400;letter-spacing:.02em;color:var(--ink)}
  .contact__title span{color:var(--olive);font-weight:500}
  .contact__rule{width:14px;height:2px;background:var(--olive);margin:8px 0 16px}
  .contact__list{list-style:none;font-size:9px;font-weight:300;line-height:1.35}
  .contact__list li{display:flex;gap:8px;align-items:flex-start;margin-bottom:9px}
  .contact__list svg{flex:none;width:10px;height:10px;margin-top:1px}

  .social{position:absolute;left:300px;top:660px;display:flex;gap:9px}
  .social span{width:15px;height:15px;border-radius:50%;background:var(--muted)}

  /* front cover */
  .front-brand{position:absolute;left:140px;top:58px;display:flex;align-items:center;gap:10px;color:var(--olive);font-weight:600;font-size:20px;letter-spacing:.02em}
  .front-brand .brand__dot{width:24px;height:24px;border-width:3px}

  .title-block{position:absolute;left:190px;top:140px;width:280px;height:566px;background:var(--lime-block)}
  .title-block__inner{position:absolute;left:30px;top:160px;right:24px;color:var(--white)}
  .title-block h1{font-size:30px;font-weight:600;line-height:1.12;letter-spacing:.04em;text-transform:uppercase}
  .title-block__rule{width:18px;height:2px;background:var(--white);margin:14px 0 16px}
  .title-block p{font-size:12px;font-weight:500;line-height:1.5}

  .web-vertical{position:absolute;left:30px;top:668px;transform:rotate(-90deg);transform-origin:left top;font-size:10px;color:var(--ink);letter-spacing:.02em;white-space:nowrap}
  .web-line{position:absolute;left:18px;top:580px;width:1px;height:140px;background:var(--olive)}
</style>
</head>
<body>
  <main class="spread">
    <div class="hero-photo" role="img" aria-label="Photograph of a hand sketching a modern building over a blue-toned architectural rendering"></div>

    <section class="panel panel--back">
      <div class="accent-band"></div>

      <div class="contact">
        <div class="brand"><span class="brand__dot"></span>Lumen Atelier</div>
        <h2 class="contact__title">CONTACT <span>INFO</span></h2>
        <div class="contact__rule"></div>
        <ul class="contact__list">
          <li><svg viewBox="0 0 10 10"><path d="M5 1a3 3 0 0 1 3 3c0 2-3 5-3 5S2 6 2 4a3 3 0 0 1 3-3z" fill="none" stroke="#a4b42a"/></svg>14 Vas. Sofias Ave, Athens 106 74</li>
          <li><svg viewBox="0 0 10 10"><rect x="1" y="2.5" width="8" height="5.5" fill="none" stroke="#a4b42a"/><path d="M1 2.5l4 3 4-3" fill="none" stroke="#a4b42a"/></svg>hello@lumenatelier.com</li>
          <li><svg viewBox="0 0 10 10"><path d="M2 1h2l1 2.5-1.2 1a5 5 0 0 0 2.7 2.7l1-1.2L9 6v2a1 1 0 0 1-1 1A7 7 0 0 1 1 2a1 1 0 0 1 1-1z" fill="none" stroke="#a4b42a"/></svg>+30 210 555 0148</li>
          <li><svg viewBox="0 0 10 10"><circle cx="5" cy="5" r="4" fill="none" stroke="#a4b42a"/><path d="M1 5h8M5 1c2 2.5 2 5.5 0 8M5 1c-2 2.5-2 5.5 0 8" fill="none" stroke="#a4b42a"/></svg>www.lumenatelier.com</li>
        </ul>
      </div>

      <div class="social" aria-label="Social links"><span></span><span></span><span></span><span></span></div>
    </section>

    <section class="panel panel--front">
      <div class="front-brand"><span class="brand__dot"></span>Lumen Atelier</div>

      <div class="title-block">
        <div class="title-block__inner">
          <h1>Lorem<br>Ipsum<br>Dolor Sit<br>Amet</h1>
          <div class="title-block__rule"></div>
          <p>consectetur adipiscing elit, sed do eiusmod tempor incididunt ut labore et dolore magna aliqua</p>
        </div>
      </div>

      <div class="web-line"></div>
      <span class="web-vertical">www.lumenatelier.com</span>
    </section>
  </main>
</body>
</html>
```